Venture Keystone - Client Appreciation Party Invitation and Poster

We need a printable invitation, a version of the same invitation that can be emailed out, and also a Poster of the invitation for our annual client appreciation party.

The location is called: The Lanternhouse. Here is a link to the location: https://www.thelanternhousevenue.example/

We like their font and their little logo that you see when you log onto this page. But we'd love to see creatively what you can come up with.

This party is for our clients who are interior designers and owners in the Hospitality industry. Here are the details which need to be included in the invitation:

Location: The Lanternhouse - 482 W Brindle Ave. Chicago IL 60614
Date/Time: Thursday August 23rd - 5:30-9:00pm
RSVP: Please RSVP to: gathering@venturekeystone.example

Then our Sponsors Logos need to be included on the bottom: I have uploaded those logos here as well as our Logo and a copy of the invitation we did for last year's party so you can see sort of what we've done in the past.

For the poster - we typically do a version of the invitation (see uploaded example of last year's poster) with the sponsor logos and the overall theme of the invitation just a bit simplified by removing the date/time/location info. We need this in a printable format which can be blown up to a 24x30 poster size.

Requirements
Must have
• use 2 to 3 colors only.
• logos of sponsors can be of the same color.

```html
<!DOCTYPE html>
<html lang="en">
<head>
<meta charset="utf-8">
<title>Venture Keystone – Client Appreciation Event</title>
<link rel="stylesheet" href="https://fonts.googleapis.com/css2?family=Ultra&family=Playball&family=Poppins:wght@500;600;700&display=swap">
<style>
:root{
  --red:#c0202f;
  --board:#2b2a2a;
  --chalk:#f4efe4;
  --gold:#f3b13e;
}
*{margin:0;padding:0;box-sizing:border-box}
html,body{width:946px;height:1200px;overflow:hidden;background:#f2f2f2}
.poster{position:relative;width:946px;height:1200px;background:radial-gradient(ellipse at 50% 40%,#363535 0%,var(--board) 70%);border:8px solid var(--red);font-family:'Poppins',sans-serif;color:var(--chalk)}
.poster__rule{position:absolute;inset:10px;border:2px solid var(--red);pointer-events:none}
.abs{position:absolute}
.ribbon{left:232px;top:46px;width:448px;height:131px;background:linear-gradient(#3a3939,#333);border-radius:60px 60px 10px 10px;opacity:.7}
.ribbon__text{left:232px;top:66px;width:448px;text-align:center;font-family:'Poppins',sans-serif;font-weight:500;font-size:40px;letter-spacing:3px;color:var(--chalk)}
.mascot{left:333px;top:159px;width:252px;height:244px;border-radius:18px;background:linear-gradient(180deg,var(--red) 0%,var(--gold) 45%,var(--gold) 70%,var(--red) 100%)}
.script{font-family:'Playball',cursive;color:var(--chalk);font-size:56px;line-height:1}
.weekend{left:106px;top:258px}
.warmup{left:600px;top:258px}
.headline{left:0;top:430px;width:930px}
.event-row{left:0;top:620px;width:930px;display:flex;justify-content:center;align-items:center;gap:18px}
.event{font-family:'Playball',cursive;font-size:80px;line-height:1;color:var(--chalk)}
.save{left:155px;top:735px;width:640px;display:flex;align-items:baseline}
.save__title{font-family:'Playball',cursive;font-size:44px;white-space:nowrap}
.save__dots{flex:1;border-bottom:3px dotted var(--chalk);margin-left:6px;transform:translateY(-6px)}
.datebox{left:161px;top:798px;width:149px;height:143px;border:3px solid var(--red);text-align:center}
.datebox__day{background:var(--red);font-weight:700;font-size:19px;height:28px;line-height:29px}
.datebox__num{font-family:'Poppins',sans-serif;font-weight:500;font-size:64px;line-height:80px;letter-spacing:-2px}
.datebox__num sup{font-size:26px;vertical-align:30px;letter-spacing:0}
.datebox__month{background:var(--red);font-weight:700;font-size:19px;letter-spacing:5px;height:33px;line-height:34px;position:absolute;bottom:0;left:0;right:0}
.details{left:346px;top:822px;font-weight:600;font-size:20px;line-height:26px}
.details__item{display:flex;gap:14px;margin-bottom:10px}
.details__item svg{flex:none;margin-top:2px}
.divider{left:119px;top:962px;width:684px;border-top:3px dotted var(--chalk)}
.rsvp{left:119px;top:984px;width:684px;text-align:center;color:var(--red);font-weight:600;font-size:18px;text-transform:uppercase;letter-spacing:.2px}
.sponsors{left:2px;top:1065px;width:926px;height:57px;background:var(--red);display:flex;justify-content:space-around;align-items:center;padding:0 16px}
.sponsor{font-family:'Poppins',sans-serif;font-weight:500;font-size:17px;color:#fff;display:flex;align-items:center;gap:7px;white-space:nowrap}
.sponsor__mark{width:14px;height:14px;background:#fff;display:inline-block}
</style>
</head>
<body>
<main class="poster">
  <div class="poster__rule"></div>

  <div class="abs ribbon" role="img" aria-label="Chalk-drawn ribbon banner"></div>
  <p class="abs ribbon__text">join us for</p>

  <p class="abs script weekend">Weekend</p>
  <div class="abs mascot" role="img" aria-label="Illustration of a festive lion dance head"></div>
  <p class="abs script warmup">Warm up</p>

  <svg class="abs headline" width="930" height="190" viewBox="0 0 930 190">
    <text x="465" y="86" text-anchor="middle" font-family="Ultra, serif" font-size="96" fill="#1a1a1a" textLength="506" lengthAdjust="spacingAndGlyphs" transform="translate(5,5)">CLIENT</text>
    <text x="465" y="86" text-anchor="middle" font-family="Ultra, serif" font-size="96" fill="var(--chalk)" textLength="506" lengthAdjust="spacingAndGlyphs">CLIENT</text>
    <text x="465" y="152" text-anchor="middle" font-family="Ultra, serif" font-size="50" fill="var(--red)" textLength="510" lengthAdjust="spacingAndGlyphs">APPRECIATION</text>
    <line x="0" x1="210" y1="178" x2="720" y2="178" stroke="var(--chalk)" stroke-width="3"/>
  </svg>

  <div class="abs event-row">
    <svg width="140" height="30" viewBox="0 0 140 30" aria-hidden="true">
      <g fill="var(--chalk)"><rect x="0" y="4" width="6" height="3"/><rect x="12" y="4" width="6" height="3"/><rect x="24" y="4" width="116" height="3"/><rect x="40" y="13" width="100" height="3"/><rect x="30" y="13" width="6" height="3"/><rect x="60" y="22" width="80" height="3"/><rect x="48" y="22" width="6" height="3"/></g>
    </svg>
    <span class="event">Event</span>
    <svg width="140" height="30" viewBox="0 0 140 30" aria-hidden="true">
      <g fill="var(--chalk)"><rect x="134" y="4" width="6" height="3"/><rect x="122" y="4" width="6" height="3"/><rect x="0" y="4" width="116" height="3"/><rect x="0" y="13" width="100" height="3"/><rect x="104" y="13" width="6" height="3"/><rect x="0" y="22" width="80" height="3"/><rect x="86" y="22" width="6" height="3"/></g>
    </svg>
  </div>

  <div class="abs save"><span class="save__title">Save the date</span><span class="save__dots"></span></div>

  <div class="abs datebox">
    <div class="datebox__day">THURSDAY</div>
    <div class="datebox__num">23<sup>rd</sup></div>
    <div class="datebox__month">AUGUST</div>
  </div>

  <div class="abs details">
    <div class="details__item">
      <svg width="24" height="24" viewBox="0 0 24 24" aria-hidden="true"><circle cx="12" cy="12" r="10" fill="none" stroke="var(--red)" stroke-width="2" stroke-dasharray="50 6"/><path d="M12 6v6l4 3" fill="none" stroke="var(--red)" stroke-width="2"/></svg>
      <span>5:30-9:00pm</span>
    </div>
    <div class="details__item">
      <svg width="24" height="28" viewBox="0 0 24 28" aria-hidden="true"><path d="M12 1C6 1 2 5.5 2 11c0 7 10 16 10 16s10-9 10-16C22 5.5 18 1 12 1z" fill="var(--red)"/><circle cx="12" cy="11" r="3.5" fill="var(--board)"/></svg>
      <span>The Lanternhouse - 482 W Brindle Ave<br>St. Chicago IL 60614</span>
    </div>
  </div>

  <div class="abs divider"></div>
  <p class="abs rsvp">RSVP: Please RSVP to: gathering@venturekeystone.example</p>

  <div class="abs sponsors">
    <span class="sponsor"><span class="sponsor__mark"></span>Norvale</span>
    <span class="sponsor">Brightwell Hospitality</span>
    <span class="sponsor">Corvin Lighting</span>
    <span class="sponsor">Meridian</span>
    <span class="sponsor">Lumora</span>
    <span class="sponsor">Ashgrove</span>
  </div>
</main>
</body>
</html>
```